Flyer for customer acquisition.

Hello, We are a sportmanagement agency from Germany and we need information flyers for customer acquisition. It should be DinA4 and should have a modern but serious design. I have uploaded a information sheet, where you can find the text and the composition, the flyer should have. I also uploaded Pictures / Images, which you can use. Of course you can use other suitable images. If they are not free, I will buy them later. On the bottom of the flyer there has been the contact information. You will find them in the download section, too. If you have questions, just write me. If I forgot something, I will update the letter :) Thank you very much!
Ich brauche zusätzliche Tage um durchzusehen

```html
<!DOCTYPE html>
<html lang="de">
<head>
<meta charset="utf-8">
<title>VELTO Nachwuchsförderung – Flyer</title>
<link rel="stylesheet" href="https://fonts.googleapis.com/css2?family=Montserrat:ital,wght@0,400;0,500;0,600;0,700;0,800;1,800&display=swap">
<style>
  :root {
    --page-bg: #d9d4cc;
    --red-light: #b3321c;
    --red-mid: #8c1c12;
    --red-deep: #5a0f0c;
    --panel: rgba(48, 8, 10, 0.78);
    --gold: #f4b53c;
    --cyan: #53c4ef;
    --white: #ffffff;
    --fine: #e6c2b6;
    --rule: #b9b3b1;
    --photo-blue: #2c5f93;
    --photo-dark: #3a3f3a;
    --photo-warm: #d9702f;
    --photo-ember: #9c2a16;
  }
  * { margin: 0; padding: 0; box-sizing: border-box; }
  html, body { width: 900px; height: 1200px; overflow: hidden; }
  body { background: var(--page-bg); font-family: "Montserrat", Arial, sans-serif; position: relative; }

  .flyer {
    position: absolute; left: 82px; top: 58px; width: 742px; height: 1050px; overflow: hidden;
    background: linear-gradient(180deg, var(--red-light) 0%, var(--red-mid) 45%, var(--red-deep) 75%, var(--red-mid) 100%);
    color: var(--white);
    box-shadow: 0 6px 18px rgba(0,0,0,.35);
  }

  .photo-player-top {
    position: absolute; left: 30px; top: 20px; width: 150px; height: 220px;
    background: linear-gradient(180deg, rgba(190, 70, 35, .55), rgba(140, 35, 20, 0));
  }

  .brand { position: absolute; left: 0; right: 0; top: 118px; text-align: center; }
  .brand-name { font-size: 44px; font-weight: 700; letter-spacing: 1px; color: var(--white); line-height: 1; }
  .brand-title { margin-top: 16px; font-size: 25px; font-weight: 800; line-height: 1; }
  .brand-tagline { margin-top: 8px; font-size: 16px; font-weight: 600; color: var(--gold); letter-spacing: .3px; }

  .content-panel {
    position: absolute; left: 0; top: 250px; width: 456px; height: 607px; background: var(--panel);
  }
  .content-panel-wide {
    position: absolute; left: 456px; top: 250px; width: 112px; height: 232px; background: var(--panel);
  }
  .panel-rule { position: absolute; left: 0; top: 857px; width: 456px; height: 8px; background: var(--rule); opacity: .8; }

  .photo-player-ball {
    position: absolute; left: 568px; top: 250px; width: 174px; height: 232px;
    clip-path: polygon(18% 0, 100% 0, 100% 100%, 18% 100%, 0 50%);
    background: linear-gradient(180deg, var(--photo-blue) 0%, var(--photo-dark) 100%);
  }
  .photo-kick {
    position: absolute; left: 456px; top: 482px; width: 286px; height: 390px;
    background: linear-gradient(160deg, var(--photo-warm) 0%, var(--photo-ember) 70%, rgba(120, 25, 15, 0) 100%);
    opacity: .75;
  }

  .services { position: absolute; left: 48px; top: 262px; width: 520px; }
  .service { position: absolute; left: 0; width: 100%; }
  .service h2 { font-size: 20px; font-weight: 600; color: var(--gold); line-height: 1.2; }
  .service p { font-size: 14px; font-weight: 500; line-height: 18.5px; }
  .service .hl { color: var(--cyan); font-weight: 600; }

  .contact { position: absolute; left: 0; right: 0; top: 880px; text-align: center; font-weight: 800; font-style: italic; font-size: 21px; line-height: 28.5px; }
  .contact .web { color: var(--gold); }

  .footnote {
    position: absolute; left: 48px; width: 650px; top: 988px;
    font-size: 8.2px; line-height: 10.5px; color: var(--fine); white-space: nowrap;
  }
</style>
</head>
<body>
  <main class="flyer">
    <div class="photo-player-top" role="img" aria-label="Fotografie: Fußballspieler mit Ball, verblasst im Hintergrund"></div>

    <header class="brand">
      <div class="brand-name">VELTO</div>
      <h1 class="brand-title">Nachwuchsförderung</h1>
      <p class="brand-tagline">Wir begleiten dich auf deinem Weg zum Profi</p>
    </header>

    <div class="content-panel"></div>
    <div class="content-panel-wide"></div>
    <div class="photo-kick" role="img" aria-label="Fotografie: Fuß mit Fußballschuh schießt einen leuchtenden Ball"></div>
    <div class="panel-rule"></div>

    <div class="photo-player-ball" role="img" aria-label="Fotografie: Spieler im blauen Trikot hält einen Fußball vor Stadionkulisse"></div>

    <section class="services">
      <article class="service" style="top:0">
        <h2>Karriereplanung</h2>
        <p><span class="hl">Wir haben deine Karriere im Blick!</span> In enger Absprache mit deinen<br>Eltern und dir leiten wir die richtigen Maßnahmen und Schritte ein,<br>um dein Ziel, Profifußballer“ zu realisieren.</p>
      </article>
      <article class="service" style="top:90px">
        <h2>Ständiger Ansprechpartner</h2>
        <p>Egal um welchen Themen es sich handelt, <span class="hl">wir sind für dich da!</span><br>Ein vertrauens volles und freundschaftliches Verhältnis ist uns<br>besonders wichtig.</p>
      </article>
      <article class="service" style="top:180px">
        <h2>Rechtsberatung/Vertragsrecht</h2>
        <p>Juristendeutsch und Kleingedrucktes? Kein Problem!<br><span class="hl">Wir helfen dir den Durchblick zu behalten</span> und<br>holen immer das Beste für dich raus.</p>
      </article>
      <article class="service" style="top:266px">
        <h2>Ausrüstung</h2>
        <p><span class="hl">Wir besorgen dir deine Ausrüstung!</span><br>Unsere Beziehungen zu den großen<br>Sportartikelherstellern ermöglichen<br>den Abschluss von Ausrüsterverträgen*.</p>
      </article>
      <article class="service" style="top:373px">
        <h2>Vorsorge</h2>
        <p>Verletzungen gehören leider zum Fußball<br>dazu.<span class="hl">Wir sichern dich ab,</span> indem wir eine<br>private Zusatzkrankenversicherung für dich<br>abschließen.</p>
      </article>
      <article class="service" style="top:480px">
        <h2>Kooperationspartner/Netzwerk</h2>
        <p>Ob Entscheidungsträger oder Experte, <span class="hl">wir kennen<br>die richtigen Leute.</span> Zusätzlich bieten wir dir eine<br>große Bandbreite an Leistungen, die du jederzeit<br>in Anspruch nehmen kannst**.</p>
      </article>
    </section>

    <address class="contact">
      <div>Tel.: 07000/5550123</div>
      <div>E-Mail: info@velto-sport.de</div>
      <div class="web">www.velto-sport.de</div>
    </address>

    <p class="footnote">*Die Entscheidung über das Zustandekommen eines Ausrüstervertrags obliegt dem jeweiligen Sportartikelhersteller. Ist ein<br>Abschlussaktuell nicht möglich, erhältst du von uns 2x pro Saison neue Fußballschuhe sowie weitere Ausrüstungsgegenstände.<br>**Personal Training, Athletik-Training, Ernährungsberatung, Sportpsychologische Betreuung, uvm.</p>
  </main>
</body>
</html>
```